IT Consulting company Needs a Logo Design and Business Cards

I need a New Logo and Business Cards for an established IT Managed Services Company that specializes in flat-rate managed IT services. We provide Design and Build, Help Desk, Onsite and Remote Support Services.

Target Market(s)

Corporate Clients

Industry/Entity Type

It Company

Logo Text

Halbrook Computer Group

Requirements
Nice to have
• Tag Line= Technology at Lightning Speed

```html
<!DOCTYPE html>
<html lang="en">
<head>
<meta charset="utf-8">
<title>Halbrook Computer Group – Business Card</title>
<link rel="stylesheet" href="https://fonts.googleapis.com/css2?family=Lato:wght@400;700;900&family=Roboto:wght@700&display=swap">
<style>
  :root {
    --stage: #1c1c1c;
    --card: #121212;
    --orange: #f59c00;
    --lime: #b5cc18;
    --silver: #d6d6d6;
    --text: #e4e4e4;
    --rule: #3a3a3a;
  }
  * { box-sizing: border-box; margin: 0; padding: 0; }
  html, body { width: 1200px; height: 900px; overflow: hidden; }
  body {
    background: var(--stage);
    font-family: "Lato", Arial, sans-serif;
    position: relative;
  }
  .card {
    position: absolute;
    left: 280px;
    width: 640px;
    height: 366px;
    background: var(--card);
    border-radius: 22px;
    box-shadow: 0 14px 30px rgba(0,0,0,.55);
  }
  .card--back { top: 60px; }
  .card--front { top: 474px; }

  /* back */
  .back-brand {
    position: absolute;
    top: 110px; left: 0; right: 0;
    display: flex; align-items: center; justify-content: center; gap: 16px;
  }
  .back-brand__square {
    width: 34px; height: 34px;
    background: var(--silver);
  }
  .back-brand__name {
    font-weight: 700; font-size: 26px; letter-spacing: 1px;
    color: var(--silver); text-transform: uppercase;
    white-space: nowrap;
  }
  .tagline {
    position: absolute;
    top: 238px; left: 0; right: 0;
    text-align: center;
    font-family: "Roboto", Arial, sans-serif;
    font-weight: 700; font-size: 15px; letter-spacing: .3px;
    color: #fff;
  }

  /* front */
  .front-brand {
    position: absolute;
    top: 42px; right: 44px;
    display: flex; align-items: center; gap: 12px;
  }
  .front-brand__square {
    width: 30px; height: 30px;
    background: var(--lime);
  }
  .front-brand__name {
    font-weight: 900; font-size: 24px; line-height: 1.05;
    color: var(--orange); text-transform: uppercase; text-align: left;
  }
  .divider {
    position: absolute;
    top: 176px; left: 240px; right: 44px;
    height: 1px; background: var(--rule);
  }
  .person {
    position: absolute;
    left: 44px; top: 158px;
  }
  .person__name {
    font-weight: 900; font-size: 24px; color: var(--orange);
    text-transform: uppercase; letter-spacing: .3px;
    white-space: nowrap;
  }
  .person__role {
    font-size: 17px; color: var(--text); margin-top: 2px;
  }
  .contacts {
    position: absolute;
    left: 44px; top: 238px;
    list-style: none;
  }
  .contacts li {
    display: flex; align-items: center; gap: 10px;
    font-size: 17px; color: var(--text); line-height: 25px;
    white-space: nowrap;
  }
  .contacts svg { width: 14px; height: 14px; flex: none; }
  .address {
    position: absolute;
    right: 44px; top: 196px;
    font-size: 16px; color: var(--text); line-height: 22px; text-align: left;
    white-space: nowrap;
  }
</style>
</head>
<body>

<section class="card card--back">
  <div class="back-brand">
    <span class="back-brand__square"></span>
    <span class="back-brand__name">Halbrook Computer Group</span>
  </div>
  <p class="tagline">TECHNOLOGY AT LIGHTNING SPEED</p>
</section>

<section class="card card--front">
  <div class="front-brand">
    <span class="front-brand__square"></span>
    <span class="front-brand__name">Halbrook<br>Computer Group</span>
  </div>

  <div class="divider"></div>

  <div class="person">
    <p class="person__name">Marcus Reed</p>
    <p class="person__role">Managing Director</p>
  </div>

  <ul class="contacts">
    <li>
      <svg viewBox="0 0 14 14" aria-hidden="true"><path fill="#f59c00" d="M3 1l2.3 2.6-1.2 1.6c.8 1.8 2 3 3.8 3.8l1.6-1.2L12 10.1 10.6 12.5C5.6 12 2 8.4 1.5 3.4z"/></svg>
      044-555 210 384
    </li>
    <li>
      <svg viewBox="0 0 14 14" aria-hidden="true"><rect x="1" y="3" width="12" height="8" fill="#f59c00"/><path d="M1 3l6 4.5L13 3" fill="none" stroke="#121212" stroke-width="1.2"/></svg>
      info@halbrookgroup.com
    </li>
    <li>
      <svg viewBox="0 0 14 14" aria-hidden="true"><circle cx="7" cy="7" r="6" fill="#f59c00"/><path d="M1 7h12M7 1c-2.5 3-2.5 9 0 12M7 1c2.5 3 2.5 9 0 12" fill="none" stroke="#121212" stroke-width="1"/></svg>
      www.halbrookgroup.com
    </li>
  </ul>

  <p class="address">18 Harbor Lane, Suite 4<br>Westfield, 20817</p>
</section>

</body>
</html>
```